Create Lanternfield HR Business Cards.

Create Business Cards for Lanternfield HR. 2 sided and Would like the back to have the logo.

Info for Business Card:
Address: 4827 Millbrook Ave Suite 230 Cleveland, Ohio 44987
Office Number: 216-555-0143
Mobile: 216-555-0192

Website: www.lanternfieldhr.example

Target Market(s)

Small to medium size businesses

Industry/Entity Type

Human Resources

Contact Information for Business Card

Company logo and information

Font styles to use
Serif
Sans Serif

Requirements
Must have
• Info for Business Card: Address: 4827 Millbrook Ave Suite 230 Cleveland, Ohio 44987 Office Number: 216-555-0143 Mobile: 216-555-0192 Website: www.lanternfieldhr.example

```html
<!DOCTYPE html>
<html lang="en">
<head>
<meta charset="utf-8">
<title>Lanternfield HR Business Cards</title>
<link href="https://fonts.googleapis.com/css2?family=Montserrat:wght@300;400;700;800&display=swap" rel="stylesheet">
<style>
  :root {
    --indigo: #2b2570;
    --indigo-deep: #241f63;
    --orange: #f7931e;
    --white: #ffffff;
    --ink-grey: #4a4a4a;
    --stage: #e9e9ee;
  }
  * { margin: 0; padding: 0; box-sizing: border-box; }
  html, body { width: 1200px; height: 800px; overflow: hidden; }
  body {
    background: var(--stage);
    font-family: "Montserrat", Arial, sans-serif;
    position: relative;
  }
  .card {
    position: absolute;
    top: 105px;
    width: 340px;
    height: 590px;
    border-radius: 26px;
    overflow: hidden;
    box-shadow: 0 10px 28px rgba(0,0,0,0.18);
  }
  .card--back {
    left: 215px;
    background: var(--indigo);
    display: flex;
    align-items: center;
    justify-content: center;
  }
  .card--front {
    left: 645px;
    background: var(--white);
  }
  .brand {
    display: flex;
    align-items: center;
    gap: 12px;
    font-weight: 800;
    letter-spacing: 0.02em;
  }
  .brand__dot {
    border-radius: 50%;
    background: var(--orange);
    flex: none;
  }
  .card--back .brand { color: var(--orange); font-size: 30px; margin-top: -120px; }
  .card--back .brand__dot { width: 34px; height: 34px; }
  .card--front .brand--main {
    position: absolute;
    top: 90px; left: 0; right: 0;
    justify-content: center;
    color: var(--indigo);
    font-size: 28px;
  }
  .card--front .brand--main .brand__dot { width: 32px; height: 32px; }
  .person {
    position: absolute;
    top: 215px; left: 0; right: 0;
    text-align: center;
  }
  .person__name {
    color: var(--indigo);
    font-weight: 700;
    font-size: 24px;
    letter-spacing: 0.01em;
    text-transform: uppercase;
  }
  .person__title {
    color: var(--orange);
    font-weight: 400;
    font-size: 19px;
    margin-top: 2px;
  }
  .icon-row {
    position: absolute;
    top: 300px; left: 30px; right: 30px;
    display: flex;
    align-items: center;
    gap: 8px;
  }
  .icon-row__rule { flex: 1; height: 1px; background: var(--indigo); }
  .icon-row__icon {
    width: 34px; height: 34px;
    border-radius: 8px;
    background: var(--indigo);
    display: flex; align-items: center; justify-content: center;
  }
  .contact {
    position: absolute;
    top: 352px; left: 0; right: 0;
    text-align: center;
    color: var(--ink-grey);
    font-weight: 300;
    font-size: 17px;
    line-height: 1.35;
  }
  .contact__address { margin-top: 14px; }
  .footer-band { position: absolute; left: 0; bottom: 0; width: 340px; height: 110px; }
  .brand--corner {
    position: absolute;
    right: 16px; bottom: 14px;
    color: var(--indigo);
    font-size: 11px;
    gap: 6px;
  }
  .brand--corner .brand__dot { width: 16px; height: 16px; }
  .brand--corner { background: var(--white); padding: 4px 8px; border-radius: 12px; }
</style>
</head>
<body>
  <section class="card card--back" aria-label="Card back">
    <div class="brand"><span class="brand__dot"></span><span>Lanternfield HR</span></div>
  </section>

  <section class="card card--front" aria-label="Card front">
    <div class="brand brand--main"><span>Lanternfield HR</span><span class="brand__dot"></span></div>

    <div class="person">
      <p class="person__name">Dorian Falkrest</p>
      <p class="person__title">Managing Director</p>
    </div>

    <div class="icon-row">
      <span class="icon-row__rule"></span>
      <span class="icon-row__icon" aria-label="Office phone">
        <svg width="20" height="20" viewBox="0 0 20 20"><path d="M3 6c0-2 2-3 7-3s7 1 7 3v1h-3V6H6v1H3z M5 9h10l1 8H4z" fill="#fff"/><circle cx="10" cy="13" r="2" fill="#2b2570"/></svg>
      </span>
      <span class="icon-row__icon" aria-label="Mobile">
        <svg width="20" height="20" viewBox="0 0 20 20"><rect x="6" y="2" width="8" height="16" rx="1.5" fill="none" stroke="#fff" stroke-width="1.8"/><circle cx="10" cy="15" r="1" fill="#fff"/></svg>
      </span>
      <span class="icon-row__icon" aria-label="Email">
        <svg width="20" height="20" viewBox="0 0 20 20"><rect x="2.5" y="5" width="15" height="10" fill="none" stroke="#fff" stroke-width="1.6"/><path d="M2.5 5l7.5 6 7.5-6" fill="none" stroke="#fff" stroke-width="1.6"/></svg>
      </span>
      <span class="icon-row__icon" aria-label="Website">
        <svg width="20" height="20" viewBox="0 0 20 20"><circle cx="10" cy="10" r="7" fill="none" stroke="#fff" stroke-width="1.6"/><path d="M3 10h14M10 3c-3 4-3 10 0 14M10 3c3 4 3 10 0 14" fill="none" stroke="#fff" stroke-width="1.2"/></svg>
      </span>
      <span class="icon-row__rule"></span>
    </div>

    <div class="contact">
      <p>216-555-0143</p>
      <p>216-555-0192</p>
      <p>info@lanternfieldhr.example</p>
      <p>www.lanternfieldhr.example</p>
      <p class="contact__address">4827 Millbrook Ave Suite<br>230 Cleveland, Ohio 44987</p>
    </div>

    <svg class="footer-band" viewBox="0 0 340 110" aria-hidden="true">
      <polygon points="0,20 230,110 0,110" fill="var(--indigo)"/>
      <line x1="0" y1="14" x2="245" y2="110" stroke="var(--orange)" stroke-width="2"/>
    </svg>
    <div class="brand brand--corner"><span>Lanternfield HR</span><span class="brand__dot"></span></div>
  </section>
</body>
</html>
```